Luxury Business Card Design for High-End Window Treatments

Gilded Vantages
Custom Plantation Shutters & Architectural Shading Systems

⸻

BACK

Daniel Forsythe
Owner

Custom Interior & Exterior Window Treatments

919-482-7034
gildedvantages.com

I have included a picture that I’m hoping we can use on the back, but I’m also wondering if you can get rid of the ladder? Should we get rid of shutters , shades and blinds underneath Gilded Vantages?

Target Market(s)

High-end residential homeowners, custom home builders, architects, interior designers, and luxury renovation clients seeking premium plantation shutters and motorized architectural shading systems.

Industry/Entity Type

Custom Window treatments

Contact Information for Business Card

Front Gilded Vantages Custom Plantation Shutters Motorized Architectural Shading Systems BACK Daniel Forsythe Owner 919-482-7034 GildedVantages.com Custom Interior & Exterior Window Treatments By Appointment

Requirements
Nice to have
• Not 100% sure on nice to halves or the color but you can definitely check out my website to get a better understanding of what I’m trying to do

```html
<!DOCTYPE html>
<html lang="en">
<head>
<meta charset="utf-8">
<title>Gilded Vantages — Business Card</title>
<link href="https://fonts.googleapis.com/css2?family=Montserrat:wght@400;500;600&display=swap" rel="stylesheet">
<style>
  :root {
    --backdrop: #c9c8c6;
    --card-black: #050505;
    --card-white: #ffffff;
    --ink: #111111;
    --cream: #e9e4d6;
    --gold: #e6b93a;
    --photo-deep: #0d1626;
    --photo-mid: #2a3a55;
    --photo-light: #6d7f98;
  }
  * { box-sizing: border-box; margin: 0; padding: 0; }
  html, body { width: 906px; height: 1200px; overflow: hidden; }
  body {
    background: var(--backdrop);
    font-family: "Montserrat", sans-serif;
    position: relative;
  }
  .card {
    position: absolute;
    left: 73px;
    width: 760px;
    height: 455px;
    overflow: hidden;
  }
  .card--front { top: 110px; background: var(--card-black); }
  .card--back { top: 635px; background: var(--card-white); }

  /* Front */
  .front-photo {
    position: absolute;
    top: 0; right: 0;
    width: 435px; height: 100%;
    background:
      linear-gradient(90deg, var(--card-black) 0%, rgba(5,5,5,0) 35%),
      linear-gradient(180deg, var(--photo-light) 0%, var(--photo-mid) 35%, var(--photo-deep) 70%, #0a0a0a 100%);
  }
  .brand-name {
    position: absolute;
    left: 52px; top: 92px;
    color: var(--cream);
    font-weight: 400;
    font-size: 50px;
    line-height: 1.05;
  }
  .brand-lines {
    position: absolute;
    left: 52px; top: 228px;
    color: var(--gold);
    font-weight: 500;
    font-size: 22px;
    word-spacing: 10px;
  }
  .front-rule {
    position: absolute;
    left: 66px; top: 298px;
    width: 230px; height: 2px;
    background: linear-gradient(90deg, rgba(255,255,255,0.2), #ffffff 60%, rgba(255,255,255,0.3));
  }
  .front-tagline {
    position: absolute;
    left: 54px; top: 340px;
    width: 680px;
    color: #ffffff;
    font-weight: 600;
    font-size: 20px;
    line-height: 1.45;
  }

  /* Back */
  .back-shapes { position: absolute; inset: 0; width: 100%; height: 100%; }
  .person-name {
    position: absolute;
    left: 52px; top: 82px;
    color: var(--ink);
    font-weight: 600;
    font-size: 33px;
  }
  .person-role {
    position: absolute;
    left: 52px; top: 126px;
    color: var(--ink);
    font-size: 20px;
  }
  .contact-list {
    position: absolute;
    left: 50px; top: 238px;
    list-style: none;
    color: var(--ink);
    font-size: 15px;
  }
  .contact-list li {
    display: flex;
    align-items: flex-start;
    gap: 14px;
    margin-bottom: 12px;
    line-height: 1.35;
  }
  .contact-list svg { width: 18px; height: 18px; flex-shrink: 0; margin-top: 1px; }
  .back-brand {
    position: absolute;
    left: 500px; top: 78px;
    width: 240px;
    text-align: center;
    color: var(--cream);
  }
  .back-brand .brand-title { font-size: 34px; line-height: 1.05; font-weight: 400; }
  .back-brand .brand-sub { color: var(--gold); font-size: 14px; font-weight: 500; margin-top: 10px; word-spacing: 6px; }
  .service-line {
    position: absolute;
    left: 500px; top: 262px;
    width: 240px;
    text-align: center;
    color: #ffffff;
    font-weight: 600;
    font-size: 21px;
    line-height: 1.3;
    letter-spacing: 1.6px;
  }
</style>
</head>
<body>
  <section class="card card--front" aria-label="Card front">
    <div class="front-photo" role="img" aria-label="Photo of a luxury home with shaded porch windows at dusk"></div>
    <div class="brand-name">Gilded<br>Vantages</div>
    <div class="brand-lines">Shutters Shades Blinds</div>
    <div class="front-rule"></div>
    <p class="front-tagline">Gilded Vantages Custom Plantation Shutters Motorized Architectural Shading Systems</p>
  </section>

  <section class="card card--back" aria-label="Card back">
    <svg class="back-shapes" viewBox="0 0 438 262" preserveAspectRatio="none" aria-hidden="true">
      <polygon points="265,0 438,0 438,262 200,262" fill="#050505"/>
      <polygon points="254,45 290,45 260,65 249,65" fill="#ffffff"/>
      <polygon points="241,95 277,95 247,115 236,115" fill="#ffffff"/>
      <polygon points="229,145 265,145 235,165 224,165" fill="#ffffff"/>
      <polygon points="217,195 253,195 223,215 212,215" fill="#ffffff"/>
    </svg>

    <h1 class="person-name">Daniel Forsythe</h1>
    <p class="person-role">Owner</p>

    <ul class="contact-list">
      <li>
        <svg viewBox="0 0 24 24"><path d="M12 2a7 7 0 0 0-7 7c0 5 7 13 7 13s7-8 7-13a7 7 0 0 0-7-7zm0 9.5A2.5 2.5 0 1 1 12 6.5a2.5 2.5 0 0 1 0 5z" fill="#111"/></svg>
        <span>418 Linden Ave Suite 12,<br>Ashbury, NC 28390</span>
      </li>
      <li>
        <svg viewBox="0 0 24 24"><path d="M6.6 10.8a15 15 0 0 0 6.6 6.6l2.2-2.2a1 1 0 0 1 1-.25 11.4 11.4 0 0 0 3.6.57 1 1 0 0 1 1 1V20a1 1 0 0 1-1 1A17 17 0 0 1 3 4a1 1 0 0 1 1-1h3.5a1 1 0 0 1 1 1c0 1.25.2 2.45.57 3.57a1 1 0 0 1-.25 1z" fill="#111"/></svg>
        <span>919-482-7034</span>
      </li>
      <li>
        <svg viewBox="0 0 24 24"><circle cx="12" cy="12" r="9" fill="none" stroke="#111" stroke-width="2"/><path d="M3 12h18M12 3c3 3 3 15 0 18M12 3c-3 3-3 15 0 18" fill="none" stroke="#111" stroke-width="1.6"/></svg>
        <span>gildedvantages.com</span>
      </li>
    </ul>

    <div class="back-brand">
      <div class="brand-title">Gilded<br>Vantages</div>
      <div class="brand-sub">Shutters Shades Blinds</div>
    </div>
    <p class="service-line">Custom Interior<br>&amp; Exterior<br>Window<br>Treatments</p>
  </section>
</body>
</html>
```